RT Advisory - Web Design Upgrade

We have recently designed a website (http://www.rtadvisory-example.com.au) which requires more creative and professional inputs. The website was designed using 'bright hosting site builder template' and it is currently available for viewing on the internet. Also, you are able to access the PDF files for the 6 main pages (i.e. Home, About, Services, Contaminated Land Management, Groundwater Management and Contact).

The current website has 17 pages, however, your design may only be required for the 6 main pages.

Currently the website background is white but we are open to other colours provided the company logo is adjusted accordingly.

The idea is to upgrade the existing design and, if possible, continue using 'bright hosting' as the preferred web host. So we are not sure if the design should be coded or uncoded...we leave it to your proficiency and advice.

Target Market(s)

Government organisations, landowners and developers, waste and utilities companies, community organisations and individuals.

Font styles to use
Sans Serif

Colors
0355a3
3176b5
9ccb3b
acd037
ffffff

Requirements
Nice to have
• Sliding images

```html
<!DOCTYPE html>
<html lang="en">
<head>
<meta charset="utf-8">
<title>RT Advisory</title>
<link rel="stylesheet" href="https://fonts.googleapis.com/css2?family=Open+Sans:ital,wght@0,400;0,600;0,700;1,700&family=Oswald:wght@400&display=swap">
<style>
:root{
  --blue-dark:#0355a3;
  --blue:#3176b5;
  --blue-light:#5b93cc;
  --green:#9ccb3b;
  --green-alt:#acd037;
  --green-text:#c4e04a;
  --olive:#3f4a1a;
  --ink:#333333;
  --white:#ffffff;
}
*{box-sizing:border-box;margin:0;padding:0}
html,body{width:928px;height:1200px;overflow:hidden}
body{position:relative;font-family:"Open Sans",Arial,sans-serif;color:var(--ink);background:var(--white)}
.abs{position:absolute}

/* header */
.site-header{left:0;top:0;width:928px;height:135px;background:linear-gradient(180deg,#e4ecf2 0%,#f4f7f9 60%,#eef2f5 100%)}
.brand{left:100px;top:12px;width:120px;display:flex;flex-direction:column;align-items:center;gap:6px}
.brand-mark{width:76px;height:76px;border-radius:50%;background:var(--blue-dark)}
.brand-name{font-size:17px;font-weight:600;color:var(--blue-dark);line-height:22px;white-space:nowrap}
.tagline{left:222px;top:36px;font-size:12.5px;font-weight:700;font-style:italic;color:var(--olive)}
.search{left:625px;top:50px;width:178px;height:25px;background:var(--white);border:1px solid #c9ced3;font-size:8px;color:#888;padding:7px 6px;letter-spacing:.3px}
.search svg{position:absolute;right:7px;top:5px}
.header-phone{left:664px;top:90px;font-size:16px;color:#222}

/* nav */
.main-nav{left:0;top:135px;width:928px;height:37px;background:linear-gradient(180deg,#2f7cc6 0%,#1d64ad 100%);border-top:2px solid #1a5ea4}
.nav-item{top:0;height:37px;line-height:37px;color:var(--white);font-size:13px;font-weight:600;text-align:center;border-right:1px solid #174f8c}
.nav-item.is-active{background:var(--green);color:var(--blue-dark);top:-4px;height:39px;line-height:43px;border-right:none;border-radius:3px 3px 0 0}

/* hero */
.hero{left:0;top:172px;width:928px;height:344px;background:linear-gradient(180deg,#8a9097 0%,#6c6a5c 45%,#6a3a2c 75%,#5a3328 100%)}
.hero-caption{left:0;top:466px;width:928px;height:50px;background:rgba(40,40,40,.6);color:var(--white);font-size:19px;padding:10px 108px}
.hero-arrow{top:326px;width:34px;height:34px;background:rgba(255,255,255,.9);border-radius:2px}

/* service cards */
.card{top:539px;width:355px;height:250px;background:var(--blue);border-radius:7px;color:var(--white);text-align:center}
.card-title{position:absolute;left:0;top:15px;width:100%;font-size:13px;font-weight:400}
.card-frame{position:absolute;left:16px;top:46px;width:324px;height:118px;background:var(--blue-light);padding:7px}
.card-photo{width:100%;height:100%}
.card-text{position:absolute;left:0;top:168px;width:100%;font-size:10.5px;line-height:15px}
.card-button{position:absolute;left:135px;top:229px;width:85px;height:25px;background:var(--green);color:var(--blue-dark);font-family:"Oswald",sans-serif;font-size:12.5px;line-height:25px;border-radius:8px 8px 0 0}
.card-shadow{top:790px;width:355px;height:20px;background:radial-gradient(ellipse at 50% 0%,rgba(0,0,0,.18),rgba(0,0,0,0) 70%)}

.statement{left:0;top:845px;width:928px;text-align:center;font-size:24.5px;line-height:36px;color:#2b2b2b;letter-spacing:-.2px}

/* footer */
.site-footer{left:0;top:933px;width:928px;height:219px;background:linear-gradient(180deg,#3a7fc3 0%,#2a73ba 40%,#0d5ea9 100%);color:var(--white)}
.footer-rule{left:0;top:46px;width:928px;border-top:1px dashed #7fa9d6}
.footer-heading{top:12px;font-family:"Oswald",sans-serif;font-size:15.5px;font-weight:400}
.footer-divider{top:60px;width:1px;height:140px;background:#4f8cc7}
.quick-links{left:101px;top:54px;list-style:none;font-size:10.5px;line-height:21.7px}
.quick-links li::before{content:"›";margin-right:9px}
.news-item{left:254px;width:185px}
.news-date{position:absolute;left:0;top:2px;width:25px;text-align:center}
.news-month{background:var(--blue-dark);font-size:8px;font-weight:700;line-height:11px}
.news-day{background:var(--green);font-size:12px;font-weight:700;line-height:17px}
.news-body{position:absolute;left:32px;top:0;font-size:9.7px;line-height:14px}
.news-title{color:var(--green-text);font-weight:700}
.contact{left:479px;top:57px;width:150px;font-size:9.7px;line-height:15px;font-style:normal}
.contact strong{font-weight:700}
.contact-line{display:flex;align-items:center;gap:6px;margin-top:12px;white-space:nowrap}
.contact-line.is-email{font-size:8.8px;letter-spacing:-.1px}
.contact-form{left:656px;top:61px}
.field{width:170px;height:24px;background:var(--white);border:1px solid #1d3f66;font-size:10px;color:#333;padding:5px 6px;margin-bottom:5px}
.field.is-tall{height:52px}
.submit{width:76px;height:23px;background:var(--green);color:var(--blue-dark);font-size:11px;font-weight:700;text-align:center;line-height:23px}

/* bottom bar */
.bottom-bar{left:0;top:1152px;width:928px;height:48px;background:var(--green);font-size:10px;color:#2a2a2a}
.social{top:1160px;width:20px;height:20px;border-radius:50%;background:#333}
</style>
</head>
<body>

<header class="abs site-header">
  <div class="abs brand"><span class="brand-mark"></span><span class="brand-name">RT Advisory</span></div>
  <p class="abs tagline">“Working to Sustain Our Environments”</p>
  <div class="abs search">SEARCH
    <svg width="14" height="14" viewBox="0 0 14 14"><circle cx="5.5" cy="5.5" r="4" fill="none" stroke="#aaa" stroke-width="1.6"/><line x1="8.5" y1="8.5" x2="13" y2="13" stroke="#aaa" stroke-width="2"/></svg>
  </div>
  <p class="abs header-phone">+61 (0)2 9000 4127</p>
</header>

<nav class="abs main-nav">
  <div class="abs nav-item is-active" style="left:102px;width:85px">HOME</div>
  <div class="abs nav-item" style="left:187px;width:108px">ABOUT US</div>
  <div class="abs nav-item" style="left:295px;width:103px">SERVICES</div>
  <div class="abs nav-item" style="left:398px;width:120px;border-right:none">CONTACT US</div>
</nav>

<section>
  <div class="abs hero" role="img" aria-label="Two field workers in hard hats and hi-vis vests lowering a groundwater probe beside orange traffic cones"></div>
  <div class="abs hero-caption">Groundwater Monitoring</div>
  <div class="abs hero-arrow" style="left:68px"><svg width="34" height="34" viewBox="0 0 34 34"><path d="M22 10 L11 17 L22 24 L18 17 Z" fill="#444"/></svg></div>
  <div class="abs hero-arrow" style="left:826px"><svg width="34" height="34" viewBox="0 0 34 34"><path d="M12 10 L23 17 L12 24 L16 17 Z" fill="#444"/></svg></div>
</section>

<section>
  <article class="abs card" style="left:102px">
    <h2 class="card-title">Contaminated Land Management</h2>
    <div class="card-frame"><div class="card-photo" role="img" aria-label="Wetland with grass at sunset under a cloudy sky" style="background:linear-gradient(180deg,#3e4046 0%,#8a8570 40%,#a9b6c4 60%,#6f8a3a 100%)"></div></div>
    <p class="card-text">Lorem ipsum dolor sit amet, consectetuer adipiscing elit,<br>sed diam nonummy nibh euismod tincidunt ut laoreet dolore<br>magna aliquam erat volutpat. Ut wisi enim ad minim</p>
    <div class="card-button">READ MORE</div>
  </article>
  <div class="abs card-shadow" style="left:102px"></div>

  <article class="abs card" style="left:471px">
    <h2 class="card-title">Groundwater Management</h2>
    <div class="card-frame"><div class="card-photo" role="img" aria-label="Drilling rig and crew installing pipes at a groundwater site" style="background:linear-gradient(180deg,#b9c7d3 0%,#8c8e78 45%,#c9a93a 70%,#b49a78 100%)"></div></div>
    <p class="card-text">Lorem ipsum dolor sit amet, consectetuer adipiscing elit,<br>sed diam nonummy nibh euismod tincidunt ut laoreet dolore<br>magna aliquam erat volutpat. Ut wisi enim ad minim</p>
    <div class="card-button">READ MORE</div>
  </article>
  <div class="abs card-shadow" style="left:471px"></div>
</section>

<p class="abs statement">We implement technical leadership in our approach, promote<br>excellence &nbsp;in our services and support practical solutions</p>

<footer class="abs site-footer">
  <div class="abs footer-rule"></div>
  <h3 class="abs footer-heading" style="left:103px">Quick Links</h3>
  <h3 class="abs footer-heading" style="left:264px">News / Updates</h3>
  <h3 class="abs footer-heading" style="left:479px">Contact Details</h3>
  <h3 class="abs footer-heading" style="left:657px">Get in Touch</h3>
  <div class="abs footer-divider" style="left:233px"></div>
  <div class="abs footer-divider" style="left:458px"></div>
  <div class="abs footer-divider" style="left:633px"></div>

  <ul class="abs quick-links"><li>Home</li><li>About Us</li><li>Services</li><li>Contact Us</li></ul>

  <div class="abs news-item" style="top:59px">
    <div class="news-date"><div class="news-month">NOV</div><div class="news-day">10</div></div>
    <div class="news-body"><div class="news-title">Duis autem vel eumsodn</div>Lorem ipsum dolor sit ametm nk<br>consectetuer adipiscing elit.</div>
  </div>
  <div class="abs news-item" style="top:109px">
    <div class="news-date"><div class="news-month">NOV</div><div class="news-day">11</div></div>
    <div class="news-body"><div class="news-title">Duis autem vel eumsodn</div>Lorem ipsum dolor sit ametm nk<br>consectetuer adipiscing elit.</div>
  </div>
  <div class="abs news-item" style="top:159px">
    <div class="news-date"><div class="news-month">NOV</div><div class="news-day">12</div></div>
    <div class="news-body"><div class="news-title">Duis autem vel eumsodn</div>Lorem ipsum dolor sit ametm nk<br>consectetuer adipiscing elit.</div>
  </div>

  <address class="abs contact">
    <strong>River &amp; Terrain Advisory<br>Pty Ltd</strong><br>48 Wattle Creek Road,<br>Lakeside, NSW 2199
    <div class="contact-line" style="margin-top:14px"><svg width="10" height="11" viewBox="0 0 10 11"><path d="M2 0 L4 3 L3 4.5 Q4.5 7 6 7.5 L7.2 6.5 L10 8.6 L8.6 11 Q3 10 0 2 Z" fill="#fff"/></svg>+61 (0)2 9000 4127</div>
    <div class="contact-line"><svg width="11" height="10" viewBox="0 0 11 10"><rect x="2.5" y="0" width="6" height="3" fill="#fff"/><rect x="0" y="3.5" width="11" height="4" fill="#fff"/><rect x="2.5" y="6" width="6" height="4" fill="#fff" stroke="#2a73ba"/></svg>+61 (0)2 9000 4128</div>
    <div class="contact-line is-email"><svg width="11" height="8" viewBox="0 0 11 8"><rect width="11" height="8" fill="#fff"/><path d="M0 0 L5.5 4.5 L11 0" fill="none" stroke="#2a73ba"/></svg>info@rtadvisory-example.com.au</div>
  </address>

  <form class="abs contact-form">
    <div class="field">Name</div>
    <div class="field">Email</div>
    <div class="field is-tall">Message</div>
    <div class="submit">SUBMIT</div>
  </form>
</footer>

<div class="abs bottom-bar">
  <span class="abs" style="left:103px;top:13px">© 2014 RT Advisory | &nbsp;All Rights Reserved</span>
  <span class="abs" style="left:435px;top:13px">ABN 12 345 678 901</span>
</div>
<span class="abs social" style="left:716px"></span>
<span class="abs social" style="left:746px"></span>
<span class="abs social" style="left:776px"></span>
<span class="abs social" style="left:806px"></span>

</body>
</html>
```